Summit Builders Web Site / Business Cards

Construction Company that specializes in Water and Fire Damage, Residential ReModels, Landscaping and Building ADU (Accessory Dwelling Unit)

Growing and changing families often need additional space, and a remodeling project can often provide that. Adding a new area, or repurposing an existing one can satisfy this requirement.

Other times, homeowners want to update the look in their kitchen or bathroom with more than just a change of cabinetry or vanity doors and drawers. Whatever your needs are, Summit Builders has skilled workers who are bonded and insured, and ready to make your dreams and visions a reality.

Target Market(s)

Home Owners

Industry/Entity Type

Construction Company

Contact Information for Business Card

Center Logo with our information on the corners

Back side to be Logo Only
Contact Info
CSLB License # 4829516
info@summitbuildersca.example
www.summitbuildersca.example

Coding

Coded - Design and coding required

Number of Pages Required

5+ page

Font styles to use
Serif
Sans Serif

Requirements
Must have
• Using our Logo Colors
Home
About Us
Services
Projects / Portfolio
Contact Us
Nice to have
• Colors matching our Logo
Should not have
• Black because it doesnt match our logo

```html
<!DOCTYPE html>
<html lang="en">
<head>
<meta charset="utf-8">
<title>Summit Builders</title>
<link href="https://fonts.googleapis.com/css2?family=Fira+Sans:wght@400;500;600;700&family=Open+Sans:wght@400;600;700&display=swap" rel="stylesheet">
<style>
:root{
  --orange:#f7630c;
  --orange-deep:#e85705;
  --orange-soft:#fbe3d4;
  --ink:#2b2623;
  --text:#4a4440;
  --muted:#8b8580;
  --paper:#ffffff;
  --mist:#f4f4f4;
  --panel:#ececec;
  --charcoal:#3a3634;
  --charcoal-2:#2f2b29;
  --line:#dcd8d5;
}
*{box-sizing:border-box;margin:0;padding:0}
html,body{width:1200px;height:3905px;overflow:hidden}
body{font-family:"Open Sans",sans-serif;color:var(--text);background:var(--paper);position:relative}
.abs{position:absolute}
h1,h2,h3,.display{font-family:"Fira Sans",sans-serif}
a{color:inherit;text-decoration:none}

/* hero */
.hero{position:absolute;left:0;top:0;width:1200px;height:648px;background:linear-gradient(180deg,#5b5566 0%,#6d6359 45%,#7b6a52 75%,#5a4c3b 100%)}
.hero-shade{position:absolute;inset:0;background:linear-gradient(90deg,rgba(40,32,28,.55),rgba(40,32,28,.15))}
.topbar{position:absolute;left:663px;top:0;width:458px;height:27px;background:var(--paper);display:flex;align-items:center;font-size:11px;color:var(--ink)}
.cert{width:138px;height:27px;background:var(--orange-soft);margin-right:14px}
.topbar .mail{flex:1}
.social{display:flex;gap:9px;padding-right:12px}
.social i{display:block;width:10px;height:10px;border-radius:50%;background:var(--ink)}
.brand{position:absolute;left:88px;top:46px;display:flex;align-items:center;gap:10px;color:#fff;font-family:"Fira Sans",sans-serif;font-weight:700;font-size:21px;letter-spacing:1px}
.brand span.mark{width:22px;height:22px;background:var(--orange)}
.nav{position:absolute;top:56px;left:0;font-size:12.5px;color:#fff}
.nav a{position:absolute;white-space:nowrap}
.phone{position:absolute;left:818px;top:56px;font-size:13px;color:#fff;font-weight:600;display:flex;gap:6px;align-items:center;white-space:nowrap}
.quote-btn{position:absolute;left:968px;top:47px;width:143px;height:30px;border:1.5px solid var(--orange);color:var(--orange);font-size:11px;display:flex;align-items:center;justify-content:center;letter-spacing:.3px}
.hero h1{position:absolute;left:156px;top:244px;width:600px;font-size:52px;line-height:63px;color:#fff;font-weight:700}
.hero p{position:absolute;left:156px;top:380px;width:560px;font-size:14.5px;line-height:22px;color:#f1ece8}
.scroll{position:absolute;left:156px;top:486px;display:flex;align-items:center;gap:14px;color:#fff;font-size:12px}
.scroll b{width:32px;height:32px;border-radius:50%;background:#fff;display:flex;align-items:center;justify-content:center}

/* shared heads */
.eyebrow{position:absolute;width:100%;text-align:center;color:var(--orange);font-size:12.5px}
.title{position:absolute;width:100%;text-align:center;font-size:33px;line-height:40px;font-weight:600;color:var(--ink)}
.outline-btn{position:absolute;border:1.5px solid #6b6561;color:var(--ink);font-size:10.5px;font-weight:600;display:flex;align-items:center;justify-content:center;gap:6px;letter-spacing:.3px;background:var(--paper)}

/* services */
.services{position:absolute;left:0;top:648px;width:1200px;height:591px;background:var(--mist)}
.svc{position:absolute;top:185px;width:342px;height:294px;text-align:center}
.svc.active{background:var(--paper);box-shadow:0 4px 18px rgba(0,0,0,.08)}
.svc svg.icon{margin-top:38px}
.svc h3{font-size:16.5px;font-weight:500;color:var(--ink);margin-top:16px;letter-spacing:.3px}
.svc p{font-size:11.5px;line-height:21px;color:var(--muted);width:270px;margin:10px auto 0}
.svc .go{width:34px;height:34px;border-radius:50%;background:var(--paper);margin:22px auto 0;display:flex;align-items:center;justify-content:center;box-shadow:0 2px 6px rgba(0,0,0,.08)}
.svc.active .go{background:var(--orange)}

/* about */
.about{position:absolute;left:0;top:1239px;width:1200px;height:562px;background:var(--paper)}
.about .tag{position:absolute;left:156px;top:101px;color:var(--orange);font-size:12.5px}
.about h2{position:absolute;left:156px;top:120px;font-size:33px;font-weight:600;color:var(--ink)}
.about p{position:absolute;left:156px;top:180px;width:390px;font-size:11.5px;line-height:21px;color:var(--muted)}
.points{position:absolute;left:156px;top:267px;list-style:none}
.points li{display:flex;align-items:center;gap:10px;height:33px;font-size:13.5px;font-weight:600;color:var(--ink);letter-spacing:.3px}
.about .backdrop{position:absolute;left:651px;top:100px;width:370px;height:397px;background:var(--panel)}
.about .photo{position:absolute;left:676px;top:76px;width:368px;height:398px;background:linear-gradient(160deg,#7fa6c8 0%,#a88a66 40%,#8b6f4d 70%,#c7a24a 100%)}

/* stats */
.stats{position:absolute;left:0;top:1801px;width:1200px;height:143px;background:linear-gradient(90deg,var(--orange-deep),var(--orange) 50%,#f47a26)}
.stat{position:absolute;top:0;width:222px;height:143px;text-align:center;color:#fff}
.stat b{display:block;font-family:"Fira Sans",sans-serif;font-size:40px;font-weight:600;margin-top:32px;line-height:48px}
.stat span{font-size:14.5px;color:#ffe6d6}
.divider{position:absolute;top:0;width:1px;height:143px;background:rgba(255,255,255,.28)}

/* gallery */
.projects{position:absolute;left:0;top:1944px;width:1200px;height:783px;background:var(--paper)}
.tile{position:absolute}
.g1{left:88px;top:151px;width:495px;height:279px;background:linear-gradient(120deg,#e9e1d2 0%,#d9cdb8 50%,#7ea6d4 100%)}
.g2{left:615px;top:151px;width:232px;height:200px;background:linear-gradient(180deg,#6a7eb6 0%,#a290a8 55%,#7c7064 100%)}
.g3{left:880px;top:151px;width:232px;height:200px;background:linear-gradient(180deg,#2f6bd1 0%,#8da7cf 45%,#9c7060 75%,#4f8a3e 100%)}
.g4{left:88px;top:463px;width:232px;height:199px;background:linear-gradient(180deg,#7cc1e0 0%,#b6b45e 45%,#3f8f2f 75%,#3a9ed0 100%)}
.g5{left:353px;top:463px;width:230px;height:199px;background:linear-gradient(120deg,#f39a5c,#f37b2c)}
.g5 .plus{position:absolute;left:96px;top:80px}
.g6{left:615px;top:383px;width:497px;height:279px;background:linear-gradient(100deg,#b9b3ad 0%,#d8cbb8 35%,#efd13a 60%,#c49a5b 85%,#8b8a94 100%)}

/* testimonial */
.testimonial{position:absolute;left:0;top:2727px;width:1200px;height:368px;background:var(--orange)}
.testimonial .mark{position:absolute;left:0;width:100%;top:58px;text-align:center}
.testimonial blockquote{position:absolute;left:320px;top:116px;width:560px;text-align:center;color:#fff;font-size:17px;line-height:32px}
.avatar{position:absolute;left:568px;top:236px;width:64px;height:64px;border-radius:50%;background:linear-gradient(160deg,#cfd6dc,#8d8f92);border:3px solid #fbd0b4}
.testimonial .who{position:absolute;width:100%;top:302px;text-align:center;color:#ffe3d2;font-size:14.5px}
.dots{position:absolute;left:1075px;top:160px;display:flex;flex-direction:column;gap:6px}
.dots i{width:8px;height:8px;border-radius:50%;border:1.3px solid rgba(255,255,255,.7)}
.dots i.on{background:#fff}

/* blog */
.blog{position:absolute;left:0;top:3095px;width:1200px;height:443px;background:var(--paper)}
.post{position:absolute;top:140px;width:284px;height:239px}
.post .date{position:absolute;left:20px;top:14px;width:42px;height:46px;background:var(--paper);text-align:center;color:var(--orange);font-family:"Fira Sans",sans-serif;font-weight:700;font-size:19px;line-height:26px}
.post .date small{display:block;font-size:8px;line-height:8px;color:var(--muted);font-weight:400;letter-spacing:.5px}
.post h3{position:absolute;left:14px;right:14px;bottom:20px;text-align:center;color:#fff;font-family:"Open Sans",sans-serif;font-size:11.5px;line-height:19px;font-weight:400}
.p1{left:156px;background:linear-gradient(160deg,#7fa6c8 0%,#a88a66 45%,#5d4a36 100%)}
.p2{left:458px;background:linear-gradient(180deg,#8c8594 0%,#8d7b64 55%,#4d4035 100%)}
.p3{left:760px;background:linear-gradient(110deg,#b9b3ad 0%,#e7c93c 45%,#9c7b4f 80%,#5c5048 100%)}

/* footer */
.footer{position:absolute;left:0;top:3538px;width:1200px;height:315px;background:var(--charcoal)}
.fcol{position:absolute;top:55px;color:#e6e1dd;font-size:12px;line-height:19.5px}
.fcol h4{font-family:"Fira Sans",sans-serif;font-size:15px;font-weight:600;color:#fff;display:flex;align-items:center;gap:7px;margin-bottom:16px}
.fcol .in{padding-left:22px}
.fcol .lbl{color:#aaa39e}
.fcol .link{color:var(--orange);text-decoration:underline}
.fcol ul{list-style:none}
.fcol ul li{height:24px}
.legal{position:absolute;left:0;top:3853px;width:1200px;height:52px;background:var(--mist)}
.legal p{position:absolute;left:88px;top:19px;font-size:11px;color:var(--muted)}
.legal .social-round{position:absolute;left:951px;top:9px;display:flex;gap:10px}
.legal .social-round i{width:34px;height:34px;border-radius:50%;border:1.3px solid #b9b3ae}
.legal .social-round i.on{background:var(--orange);border-color:var(--orange)}
</style>
</head>
<body>

<header class="hero">
  <div class="hero-shade" role="img" aria-label="Photo of a large construction site with tower cranes and apartment blocks under an evening sky"></div>
  <div class="topbar">
    <span class="cert"></span>
    <span class="mail">e: hello@summitbuildersca.example</span>
    <span class="social"><i></i><i></i><i></i><i></i></span>
  </div>
  <a class="brand" href="#"><span class="mark"></span>SUMMIT BUILDERS</a>
  <nav class="nav">
    <a style="left:372px">Home</a>
    <a style="left:444px">Services</a>
    <a style="left:528px">About Us</a>
    <a style="left:618px">Our Projects</a>
    <a style="left:728px">Contact Us</a>
  </nav>
  <div class="phone">
    <svg width="13" height="13" viewBox="0 0 24 24"><path d="M6.6 10.8a15 15 0 0 0 6.6 6.6l2.2-2.2c.3-.3.7-.4 1-.2 1.1.4 2.3.6 3.6.6.6 0 1 .4 1 1V20c0 .6-.4 1-1 1A17 17 0 0 1 3 4c0-.6.4-1 1-1h3.5c.6 0 1 .4 1 1 0 1.2.2 2.4.6 3.6.1.3 0 .7-.2 1z" fill="#fff"/></svg>
    +1 555 014 2278
  </div>
  <a class="quote-btn" href="#">REQUEST A QUOTE</a>
  <h1>Landscaping and Building ADU</h1>
  <p>Lorem ipsum is simply dummy text of the printing and typesetting industry, Lorem ipsum has been the industry's standard dummy text, when an unknown printer took a galley of type and scrambled.</p>
  <div class="scroll">
    <b><svg width="12" height="12" viewBox="0 0 12 12"><path d="M3 4.5l3 3 3-3" stroke="#f7630c" stroke-width="1.6" fill="none"/></svg></b>
    KEEP ON SCROLLING
  </div>
</header>

<section class="services">
  <div class="eyebrow" style="top:52px">What We do</div>
  <h2 class="title" style="top:74px">Delivering the Best Nationwide<br>Summit Builders</h2>

  <article class="svc" style="left:88px">
    <svg class="icon" width="34" height="48" viewBox="0 0 34 48"><path d="M10 14h14v30H10z M13 14V8h8v6 M21 9l8-4 M14 22h6v12h-6z" fill="none" stroke="#6b6561" stroke-width="2.2"/></svg>
    <h3>Water &amp; Fire Damage Solution</h3>
    <p>Lorem ipsum is simply dummy text of the printing and typesetting industry. lorem ipsum has been standard dummy text</p>
    <div class="go"><svg width="12" height="12" viewBox="0 0 12 12"><path d="M2 6h8M7 3l3 3-3 3" stroke="#f7630c" stroke-width="1.4" fill="none"/></svg></div>
  </article>

  <article class="svc active" style="left:429px">
    <svg class="icon" width="52" height="48" viewBox="0 0 52 48"><path d="M4 46V14h16v32 M20 46V4h28v42 M2 46h48 M9 20h6M9 28h6M9 36h6M26 12h4M36 12h4M26 20h4M36 20h4M26 28h4M36 28h4M26 36h4M36 36h4" fill="none" stroke="#f7630c" stroke-width="2.4"/></svg>
    <h3>Residential ReModels</h3>
    <p>Lorem ipsum is simply dummy text of the printing and typesetting industry. lorem ipsum has been standard dummy text</p>
    <div class="go"><svg width="12" height="12" viewBox="0 0 12 12"><path d="M2 6h8M7 3l3 3-3 3" stroke="#fff" stroke-width="1.4" fill="none"/></svg></div>
  </article>

  <article class="svc" style="left:770px">
    <svg class="icon" width="48" height="48" viewBox="0 0 48 48"><path d="M8 44V22M15 44V14M22 44V8M28 44V8M34 44V14M41 44V22" stroke="#6b6561" stroke-width="3.2"/><circle cx="25" cy="6" r="2" fill="#6b6561"/></svg>
    <h3>Landscaping and Building ADU</h3>
    <p>Lorem ipsum is simply dummy text of the printing and typesetting industry. lorem ipsum has been standard dummy text</p>
    <div class="go"><svg width="12" height="12" viewBox="0 0 12 12"><path d="M2 6h8M7 3l3 3-3 3" stroke="#f7630c" stroke-width="1.4" fill="none"/></svg></div>
  </article>

  <a class="outline-btn" href="#" style="left:520px;top:522px;width:160px;height:31px">EXPLORE MORE <svg width="8" height="8" viewBox="0 0 8 8"><path d="M1 1l3 3-3 3M4 1l3 3-3 3" stroke="#2b2623" fill="none"/></svg></a>
</section>

<section class="about">
  <div class="tag">About Us</div>
  <h2>Who We are</h2>
  <p>Lorem Ipsum is simply dummy text of the printing and typesetting industry. Lorem Ipsum has been the industry's standard dummy text ever since the 1500s, when an unknown printer.</p>
  <ul class="points">
    <li><svg width="15" height="15" viewBox="0 0 24 24"><path d="M12 2l3 6.8 7.4.7-5.6 4.9 1.7 7.3L12 17.8 5.5 21.7l1.7-7.3L1.6 9.5 9 8.8z" fill="#f7630c"/></svg>WE'VE REPUTION FOR EXCELLENCE</li>
    <li><svg width="15" height="15" viewBox="0 0 24 24"><path d="M7 11v10H3V11zM7 11l4-8c2 0 3 1 3 3v3h6c1 0 2 1 2 2l-2 8c0 1-1 2-2 2H7" fill="none" stroke="#f7630c" stroke-width="1.8"/></svg>GUIDED BY COMMITMENT</li>
    <li><svg width="15" height="15" viewBox="0 0 24 24"><path d="M2 11l5-5 5 3 5-3 5 5-10 8z" fill="none" stroke="#f7630c" stroke-width="1.8"/></svg>WE BUILD PARTNERSHIPS</li>
    <li><svg width="15" height="15" viewBox="0 0 24 24"><circle cx="8" cy="8" r="3.5" fill="none" stroke="#f7630c" stroke-width="1.8"/><circle cx="17" cy="9" r="3" fill="none" stroke="#f7630c" stroke-width="1.8"/><path d="M2 20c0-4 3-6 6-6s6 2 6 6M14 19c0-3 1.5-5 3.5-5s4.5 2 4.5 5" fill="none" stroke="#f7630c" stroke-width="1.8"/></svg>A TEAM OF PROFESSIONALS</li>
  </ul>
  <a class="outline-btn" href="#" style="left:156px;top:417px;width:127px;height:30px">LEARN MORE <svg width="8" height="8" viewBox="0 0 8 8"><path d="M1 1l3 3-3 3M4 1l3 3-3 3" stroke="#2b2623" fill="none"/></svg></a>
  <div class="backdrop"></div>
  <div class="photo" role="img" aria-label="Photo of two workers in hard hats cutting timber with a circular saw"></div>
</section>

<section class="stats">
  <div class="stat" style="left:156px"><b>53</b><span>Total Projects</span></div>
  <div class="divider" style="left:377px"></div>
  <div class="stat" style="left:377px"><b>371</b><span>Staff Members</span></div>
  <div class="divider" style="left:599px"></div>
  <div class="stat" style="left:600px"><b>15</b><span>Working in States</span></div>
  <div class="divider" style="left:821px"></div>
  <div class="stat" style="left:821px"><b>2,600</b><span>Hours for Work</span></div>
</section>

<section class="projects">
  <div class="eyebrow" style="top:49px">Projects</div>
  <h2 class="title" style="top:70px">Projects Gallery</h2>
  <div class="tile g1" role="img" aria-label="Photo of a curved high school building with glass facade"></div>
  <div class="tile g2" role="img" aria-label="Photo of a two-storey suburban house at dusk"></div>
  <div class="tile g3" role="img" aria-label="Photo of a brick family home with a green lawn"></div>
  <div class="tile g4" role="img" aria-label="Photo of a villa with gardens beside a river"></div>
  <div class="tile g5" role="img" aria-label="Photo of a high school building under an orange hover overlay">
    <svg class="plus" width="40" height="40" viewBox="0 0 40 40"><path d="M20 0v40M0 20h40" stroke="#fff" stroke-width="1.5"/></svg>
  </div>
  <div class="tile g6" role="img" aria-label="Photo of a worker holding a yellow hard hat beside a tool belt"></div>
  <a class="outline-btn" href="#" style="left:527px;top:704px;width:144px;height:31px">VIEW ALL WORK</a>
</section>

<section class="testimonial">
  <div class="mark"><svg width="46" height="32" viewBox="0 0 46 32"><path d="M4 30V18C4 8 10 3 18 2M26 30V18C26 8 32 3 40 2" stroke="#fff" stroke-width="3.5" fill="none"/><rect x="4" y="17" width="14" height="13" fill="none" stroke="#fff" stroke-width="3.5"/><rect x="26" y="17" width="14" height="13" fill="none" stroke="#fff" stroke-width="3.5"/></svg></div>
  <blockquote>Lorem ipsum dolor sit amet, consectetur adipiscing elit, sed do eiusmod tempor incididunt ut labore et dolore magna aliqua. Ut enim ad minim veniam, exercitation ullamco laboris nisi ...</blockquote>
  <div class="avatar" role="img" aria-label="Portrait photo of the client"></div>
  <div class="who">Daniel Whitmore</div>
  <div class="dots"><i class="on"></i><i></i><i></i><i></i></div>
</section>

<section class="blog">
  <div class="eyebrow" style="top:48px">Our Blogs</div>
  <h2 class="title" style="top:70px">Latest News</h2>
  <article class="post p1" role="img" aria-label="Photo of workers cutting timber on site">
    <div class="date">10<small>DEC</small></div>
    <h3>LOREM IPSUM IS SIMPLY DUMMY TEXT OF THE PRINTING AND TYPESETTING...</h3>
  </article>
  <article class="post p2" role="img" aria-label="Photo of tower cranes over a building site">
    <div class="date">05<small>DEC</small></div>
    <h3>LOREM IPSUM IS SIMPLY DUMMY TEXT OF THE PRINTING AND TYPESETTING...</h3>
  </article>
  <article class="post p3" role="img" aria-label="Photo of a hard hat and tool belt">
    <div class="date">24<small>NOV</small></div>
    <h3>LOREM IPSUM IS SIMPLY DUMMY TEXT OF THE PRINTING AND TYPESETTING...</h3>
  </article>
</section>

<footer class="footer">
  <div class="fcol" style="left:133px;width:260px">
    <h4><svg width="14" height="12" viewBox="0 0 14 12"><rect x="1" y="1" width="12" height="10" fill="none" stroke="#f7630c" stroke-width="1.4"/><path d="M3 4h5M3 7h8" stroke="#f7630c" stroke-width="1.2"/></svg>Contact Us</h4>
    <div class="in">
      e. <span class="link">hello@summitbuildersca.example</span><br>
      <div style="height:10px"></div>
      <span class="lbl">Phone Number:</span><br>
      Office: 555-014-2278<br>
      Direct : 555-013-0962<br>
      Fax : 555-016-7210<br>
      <div style="height:10px"></div>
      <span class="lbl">Location:</span><br>
      412 Orchard Crest Ave Lakeview,<br>CA 90000
    </div>
  </div>
  <div class="fcol" style="left:527px;width:180px">
    <h4><svg width="13" height="13" viewBox="0 0 14 14"><path d="M6 8l2-2M5 5l2-2a2.5 2.5 0 0 1 4 4l-2 2M9 9l-2 2a2.5 2.5 0 0 1-4-4l2-2" fill="none" stroke="#f7630c" stroke-width="1.4"/></svg>Quick Links</h4>
    <ul class="in">
      <li>Home</li><li>About Us</li><li>Services</li><li>Our Projects</li><li>Contact Us</li>
    </ul>
  </div>
  <div class="fcol" style="left:762px;width:300px">
    <h4><svg width="13" height="13" viewBox="0 0 14 14"><circle cx="7" cy="7" r="5.8" fill="none" stroke="#f7630c" stroke-width="1.4"/><path d="M7 3.5V7l2.5 1.5" stroke="#f7630c" stroke-width="1.4" fill="none"/></svg>Working Hours</h4>
    <div class="in" style="font-size:11.5px;line-height:17.5px">
      we work 7 days a week, every day excluding major holidays. contact us if you have an emergency, with our hotline and contact form.
      <div style="height:14px"></div>
      <div style="line-height:23px">monday - friday : <b>10:00 – 16:00</b><br>saturday : <b>12:00 – 15:00</b><br>sunday and holidays : <b>09:00 – 12:00</b></div>
    </div>
  </div>
</footer>

<div class="legal">
  <p>© 2020 Summit Builders - All rights reserved.</p>
  <div class="social-round"><i></i><i class="on"></i><i></i><i></i></div>
</div>

</body>
</html>
```